Telecom company needs marketing flyers

We need 3 different flyers to describe our product and how to qualify for the program. This our website to use for the logo and color scheme https://www.brivolinkmobile.com, however do not use the mascot on the flyer.

Attached are examples of a competitors flyers.

```html
<!DOCTYPE html>
<html lang="en">
<head>
<meta charset="utf-8">
<title>Brivolink Mobile – Limited Time Deal Flyer</title>
<link rel="stylesheet" href="https://fonts.googleapis.com/css2?family=Lato:wght@400;700;900&display=swap">
<style>
  :root {
    --navy: #0d2a5c;
    --navy-deep: #081d45;
    --blue: #1b96e0;
    --sky: #2aa4ec;
    --ink: #0f1f3d;
    --paper: #ffffff;
    --muted: #e9eef5;
  }
  * { box-sizing: border-box; margin: 0; padding: 0; }
  html, body { width: 900px; height: 1200px; overflow: hidden; }
  body { background: var(--paper); font-family: "Lato", Arial, sans-serif; color: var(--ink); }

  .flyer { position: relative; width: 900px; height: 1200px; overflow: hidden; background: var(--paper); }

  .side-panel {
    position: absolute; left: 0; top: 250px; width: 470px; height: 950px;
    background: radial-gradient(circle at 40% 85%, #1d4f9a 0%, var(--navy) 45%, var(--navy-deep) 100%);
    border-top-right-radius: 235px;
  }

  .hero-photo {
    position: absolute; left: 0; top: 22px; width: 476px; height: 476px;
    border-radius: 50%; border: 18px solid var(--sky);
    background: linear-gradient(160deg, #e8f1fb 0%, #c4d8ee 40%, #8fa9c6 75%, #5d6f84 100%);
  }

  .features { position: absolute; left: 36px; top: 580px; width: 410px; list-style: none; }
  .features li {
    position: relative; padding-left: 28px; margin-bottom: 22px;
    color: #fff; font-size: 16px; line-height: 1.35;
  }
  .features li::before {
    content: ""; position: absolute; left: 0; top: 4px; width: 14px; height: 14px; border-radius: 50%;
    background: var(--sky);
  }
  .features li.alt::before { background: #fff; }

  .brand { position: absolute; left: 493px; top: 96px; width: 340px; text-align: right; color: var(--blue); font-weight: 400; }
  .brand-name { font-size: 50px; letter-spacing: 8px; line-height: 1; text-align: left; }
  .brand-sub { font-size: 18px; letter-spacing: 4px; margin-top: 4px; }

  .headline { position: absolute; left: 505px; top: 222px; width: 355px; text-align: center; font-weight: 900; line-height: 0.98; }
  .headline span { display: block; font-size: 56px; }
  .headline .dark { color: var(--ink); }
  .headline .light { color: var(--sky); }
  .headline .big { font-size: 72px; }

  .web-bar {
    position: absolute; left: 500px; top: 478px; width: 400px; height: 36px;
    background: var(--sky); border-radius: 18px 0 0 18px;
    color: #fff; font-weight: 700; font-size: 18px; letter-spacing: 1.5px;
    display: flex; align-items: center; padding-left: 36px;
  }

  .intro {
    position: absolute; left: 504px; top: 538px; width: 366px;
    font-size: 16px; font-weight: 700; line-height: 1.65; text-align: justify; color: var(--ink);
  }

  .offer-card {
    position: absolute; left: 74px; top: 850px; width: 792px; height: 278px;
    background: var(--paper); border-radius: 10px;
    box-shadow: 0 6px 18px rgba(0,0,0,0.35);
    padding: 40px 0 0 40px;
  }
  .offer-top { font-size: 34px; font-weight: 900; color: var(--navy); letter-spacing: 0.3px; }
  .offer-main { font-size: 98px; font-weight: 900; color: var(--sky); line-height: 0.95; letter-spacing: 1px; }
  .offer-sub { font-size: 25px; font-weight: 900; color: var(--navy); margin-top: 2px; }
  .offer-call { font-size: 25px; color: var(--ink); margin-top: 12px; padding-left: 48px; }

  .phone {
    position: absolute; left: 592px; top: 717px; width: 226px; height: 446px;
    background: #0b0b0d; border-radius: 24px; padding: 28px 10px 30px;
    box-shadow: 0 6px 16px rgba(0,0,0,0.35);
  }
  .phone::before {
    content: ""; position: absolute; left: 50%; top: 11px; width: 40px; height: 5px;
    margin-left: -20px; border-radius: 3px; background: #2a2a2e;
  }
  .phone-screen {
    width: 100%; height: 100%; border-radius: 4px;
    background: linear-gradient(180deg, #9fc3e8 0%, #6fa6dc 35%, #2f6fb5 65%, #163a6e 100%);
  }
</style>
</head>
<body>
<main class="flyer">
  <div class="side-panel"></div>
  <div class="hero-photo" role="img" aria-label="Photo of cell towers with antennas against a cloudy sky"></div>

  <ul class="features">
    <li>More data means more email, more video conferencing, more Internet!</li>
    <li class="alt">Fast, flexible 5G Network.</li>
    <li>Mobile hotspot included means you can connect other devices to your ClearLine Service.</li>
    <li class="alt">Cellular Connectivity lets you take internet anywhere there is coverage</li>
  </ul>

  <div class="brand">
    <div class="brand-name">BRIVOLINK</div>
    <div class="brand-sub">MOBILE</div>
  </div>

  <h1 class="headline">
    <span class="dark">GET YOUR</span>
    <span class="light">LIMITED</span>
    <span class="light">TIME DEAL</span>
    <span class="dark big">TODAY!</span>
  </h1>

  <div class="web-bar">www.brivolinkmobile.com</div>

  <p class="intro">We understand the importance of having great customer service. Our support specialists are here to help you at any time with your questions and needs! Discover how Brivolink Mobile can help keep you connected</p>

  <section class="offer-card">
    <div class="offer-top">LOW PRICES WITH HIGH</div>
    <div class="offer-main">QUALITY</div>
    <div class="offer-sub">SERVICE &amp; BEST IN CLASS SUPPORT</div>
    <div class="offer-call">call us today +800-555-0142</div>
  </section>

  <div class="phone">
    <div class="phone-screen" role="img" aria-label="City skyline at dusk with glowing network connection arcs"></div>
  </div>
</main>
</body>
</html>
```